Regional Sales Company Needs Professional Document Design

We are an American Midwest company that needs clean, polished document layouts that effectively communicate the most critical information to the recipient. This project is specifically for a sales quote, but additional documents (subsequent work) need a consistent look. Our primary design guidelines are: 1) Use the same colors and logos provided. 2) minimize the amount of space the header occupies on the document. 3) Prioritize the information as it has been numbered in the attachment (1 - 5). 4) Redesign the footer logo/image. The information must stay the same, but present it as you see fit.

I have attached a draft and an annotation layout. The draft shows the overall structure and information on the document. The Annotation layout has the numbering referenced and some additional notes.

Industry/Entity Type

HVAC Supplier

Colors
0054AA
0677BA
7BADD7
CADEEF
E8F1F8

Requirements
Must have
• Maintain overall structure of draft. E.g. No left to right documents

```html
<!DOCTYPE html>
<html lang="en">
<head>
<meta charset="utf-8">
<title>Sales Quote Q000039</title>
<link href="https://fonts.googleapis.com/css2?family=Poppins:wght@400;500;600;700&display=swap" rel="stylesheet">
<style>
:root{
  --brand-blue:#0b4a80;
  --brand-orange:#f7941d;
  --charcoal:#444446;
  --ink:#1e1e20;
  --row-light:#e9eaec;
  --row-lighter:#f3f3f5;
  --row-mid:#dcdde0;
  --stage:#e4e4e4;
  --paper:#ffffff;
}
*{box-sizing:border-box;margin:0;padding:0}
html,body{width:1058px;height:1200px;overflow:hidden}
body{background:var(--stage);font-family:'Poppins',sans-serif;color:var(--ink);position:relative}
.quote-sheet{position:absolute;left:84px;top:24px;width:890px;height:1151px;background:var(--paper);box-shadow:0 6px 24px rgba(0,0,0,.18)}

/* header */
.brand{position:absolute;left:52px;top:62px;display:flex;align-items:center;gap:12px}
.brand-dot{width:58px;height:58px;border-radius:50%;background:var(--brand-blue)}
.brand-name{font-size:25px;font-weight:600;line-height:1.05;color:var(--brand-blue)}
.divider{position:absolute;top:66px;width:1px;height:80px;background:#d4d4d4}
.client{position:absolute;left:388px;top:49px;width:230px}
.client-name{font-size:16px;font-weight:700;line-height:20px;color:var(--brand-blue)}
.client-addr{display:flex;gap:4px;margin-top:3px;font-size:13px;line-height:16.5px}
.client-addr svg{flex:none;margin-top:3px}
.client-eng{margin-top:7px;font-size:13px}
.client-eng b{color:var(--brand-blue);font-weight:600}
.quote-meta{position:absolute;left:642px;top:52px;width:196px}
.quote-tag{display:flex;height:22px;font-size:13px}
.quote-tag .label{width:83px;background:var(--brand-orange);color:#fff;font-weight:600;padding-left:14px;line-height:22px}
.quote-tag .num{flex:1;background:var(--charcoal);color:#e8e8e8;padding-left:22px;line-height:22px}
.quote-dates{margin-top:8px;font-size:11px;line-height:14px}
.quote-dates b{color:var(--brand-blue);font-weight:600}

/* table */
.items{position:absolute;left:52px;top:177px;width:785px}
.items-head{display:grid;grid-template-columns:174px 63px 548px;height:25px;background:var(--charcoal);color:#fff;font-size:13.5px;font-weight:600;line-height:25px;text-align:center}
.item{display:grid;grid-template-columns:174px 63px 548px}
.item .maker{background:var(--paper);padding:20px 0 0 0;display:flex;align-items:center;gap:6px;height:max-content}
.maker-mark{width:12px;height:12px;background:var(--brand-blue)}
.maker-name{font-size:17px;font-weight:700;color:var(--brand-blue)}
.maker-name.dark{color:var(--ink)}
.item .qty{text-align:center;font-size:12.5px;padding-top:23px}
.item .desc{padding:20px 20px 0 22px;font-size:13.4px;line-height:17.5px}
.desc .note{margin-top:6px}
.totals{display:grid;grid-template-columns:315px 1fr;margin-top:16px}
.totals .bod{font-weight:600}
.row-1{height:169px}
.row-1 .qty{background:var(--row-lighter)}
.row-1 .desc{background:var(--row-light)}
.row-2{height:358px}
.row-2 .qty,.row-2 .desc{background:var(--row-mid)}
.row-2 .totals{margin-top:30px}
.row-3{height:231px}
.row-3 .qty{background:var(--row-lighter)}
.row-3 .desc{background:var(--row-light)}
.row-3 .totals{margin-top:7px}

/* footer */
.footer-tagline{position:absolute;left:0;top:1014px;width:890px;height:33px;background:#3a3a3c;color:#fff;font-size:15px;font-weight:600;font-style:italic;text-align:center;line-height:33px}
.footer-offices{position:absolute;left:0;top:1047px;width:890px;height:104px;background:var(--brand-blue);color:#fff}
.office{position:absolute;top:12px;font-size:11px;line-height:14px}
.office h3{font-size:14px;font-weight:600;line-height:18px}
.office p{display:flex;gap:4px}
.office svg{flex:none;margin-top:3px}
.office .indent{padding-left:15px}
.office .phone{font-weight:700;margin-top:2px}
.office-sep{position:absolute;top:14px;width:1px;height:64px;background:rgba(255,255,255,.35)}
</style>
</head>
<body>
<main class="quote-sheet">
  <header>
    <div class="brand">
      <span class="brand-dot"></span>
      <span class="brand-name">Northaire<br>Supply, Inc.</span>
    </div>
    <span class="divider" style="left:364px"></span>
    <section class="client">
      <div class="client-name">Maple Ridge<br>Care Center</div>
      <div class="client-addr">
        <svg width="11" height="11" viewBox="0 0 12 12"><circle cx="6" cy="6" r="5" fill="none" stroke="#0b4a80" stroke-width="2"/><circle cx="6" cy="6" r="1.8" fill="#0b4a80"/></svg>
        <span>1850 Harvest Oak Lane,<br>Canton, OH, 44718</span>
      </div>
      <div class="client-eng"><b>Engineer:</b> Ridgeline Engineering</div>
    </section>
    <span class="divider" style="left:618px"></span>
    <section class="quote-meta">
      <div class="quote-tag"><span class="label">Quote:</span><span class="num">Q000039</span></div>
      <div class="quote-dates">
        <div><b>Quote Date:</b> 12/31/2024</div>
        <div><b>Project Bid Date:</b> 12/31/2024</div>
        <div><b>Plan Date:</b> 12/31/2024</div>
        <div><b>Quote Rev:</b> 00</div>
        <div><b>Addendum:</b> 1</div>
      </div>
    </section>
  </header>

  <section class="items">
    <div class="items-head"><span>Manufacturer</span><span>Qty</span><span>Description</span></div>

    <div class="item row-1">
      <div class="maker"><span class="maker-name dark">Kestrel Air</span></div>
      <div class="qty">463</div>
      <div class="desc">
        <div>Pieces of Kestrel Air Distribution with Standard White Finish</div>
        <div>&nbsp;• Dampers included per the schedule IF there is NO CRD</div>
        <div>&nbsp;• If a Grille has a CRD, NO OBD included (see CRD's)</div>
        <div>&nbsp;Estimated Lead-time to ship: 3-4 weeks + Transit Time from Factory</div>
        <div class="totals">
          <span class="bod">Kestrel Air Products Inc. is Basis of Design</span>
          <span>Total with Full Freight<br>Allowed <b>$18,850</b></span>
        </div>
      </div>
    </div>

    <div class="item row-2">
      <div class="maker"><span class="maker-mark"></span><span class="maker-name">BRIGHTLINE</span></div>
      <div class="qty">2</div>
      <div class="desc">
        <div>Brightline DOAS Units (Dedicated Outdoor Air System) with Weatherhood, Return Air Intake, Expansion Board, Frost control, Outdoor/Exhaust MERV8 Filters, Supply MERV13 Filters, Outdoor Dampers, End Switch, Painted Finish, VFD Control, Economizer, Microprocessor Controls, Duct Sensors, Dirty Filter Sensor, Rotation Sensor, Phase and Brown Out Protection, Disconnect Switch, Hail Guards, Condensate Overflow Switch, Spare Energy Wheel Belt, 12:1 Turndown, DX Cooling, Inverter Scroll Compressor, Modulating Hot Gas Reheat, Lead EC Condenser Fan and 14" High FLAT Roof Curbs per Note 18 (DOAS-1,2)</div>
        <div class="note">• Includes Unit Warranty &amp; Labor Warranty</div>
        <div class="note">NOTE: Duct Adapter is NOT included - removed by BL<br>Estimated Lead-time to ship: 9 weeks + Transit Time from Factory</div>
        <div class="totals">
          <span class="bod">Brightline Fan Corporation<br>is Basis of Design</span>
          <span>Total with Full Freight<br>Allowed <b>$157,000</b></span>
        </div>
      </div>
    </div>

    <div class="item row-3">
      <div class="maker"><span class="maker-mark"></span><span class="maker-name">BRIGHTLINE</span></div>
      <div class="qty">1</div>
      <div class="desc">
        <div>ADD - for DOAS Start-Up and Start-Up Dispatch</div>
        <div class="totals">
          <span></span>
          <span>Price includes (1) trip<br>charge <b>$2,550</b></span>
        </div>
      </div>
    </div>
  </section>

  <footer>
    <div class="footer-tagline">Partnering with you: Delivering Solutions and Service</div>
    <div class="footer-offices">
      <div class="office" style="left:98px">
        <h3>Cleveland</h3>
        <p><svg width="10" height="10" viewBox="0 0 12 12"><circle cx="6" cy="6" r="5" fill="none" stroke="#fff" stroke-width="2"/><circle cx="6" cy="6" r="1.8" fill="#fff"/></svg><span>2210 Canal Ridge Road<br>Broadview Heights, Ohio 44147</span></p>
        <p class="phone"><svg width="10" height="10" viewBox="0 0 12 12"><circle cx="6" cy="6" r="5" fill="none" stroke="#fff" stroke-width="1.6"/><path d="M4 3.5l1.2 1.4-.6.8c.4.8 1 1.4 1.8 1.8l.8-.6 1.4 1.2-.8 1c-2.3-.4-4-2.1-4.4-4.4z" fill="#fff"/></svg><span>440-555-0142</span></p>
      </div>
      <span class="office-sep" style="left:339px"></span>
      <div class="office" style="left:396px">
        <h3>Columbus</h3>
        <p><svg width="10" height="10" viewBox="0 0 12 12"><circle cx="6" cy="6" r="5" fill="none" stroke="#fff" stroke-width="2"/><circle cx="6" cy="6" r="1.8" fill="#fff"/></svg><span>745 Linden Park Avenue<br>Columbus, Ohio 43201</span></p>
        <p class="phone"><svg width="10" height="10" viewBox="0 0 12 12"><circle cx="6" cy="6" r="5" fill="none" stroke="#fff" stroke-width="1.6"/><path d="M4 3.5l1.2 1.4-.6.8c.4.8 1 1.4 1.8 1.8l.8-.6 1.4 1.2-.8 1c-2.3-.4-4-2.1-4.4-4.4z" fill="#fff"/></svg><span>614-555-0187</span></p>
      </div>
      <span class="office-sep" style="left:599px"></span>
      <div class="office" style="left:647px">
        <h3>Toledo</h3>
        <p><svg width="10" height="10" viewBox="0 0 12 12"><circle cx="6" cy="6" r="5" fill="none" stroke="#fff" stroke-width="2"/><circle cx="6" cy="6" r="1.8" fill="#fff"/></svg><span>5120 S. Meadowbrook Way<br>Perrysburg, Ohio 43551</span></p>
        <p class="phone"><svg width="10" height="10" viewBox="0 0 12 12"><circle cx="6" cy="6" r="5" fill="none" stroke="#fff" stroke-width="1.6"/><path d="M4 3.5l1.2 1.4-.6.8c.4.8 1 1.4 1.8 1.8l.8-.6 1.4 1.2-.8 1c-2.3-.4-4-2.1-4.4-4.4z" fill="#fff"/></svg><span>419-555-0163</span></p>
      </div>
    </div>
  </footer>
</main>
</body>
</html>
```